Alternative Health Practice - Website redesign

With regard to the welcome image, stock photos can't show the faces of other people. And please don't submit a design for a one-page website.
Hello, I am redesigning a website and need some help from a professional.
The old website is here: peter-lindqvist.net (pls note I don't want to reuse the welcome photo from the old site). Much of the written content will remain the same, so note that I also need a page layout/text colour etc that works for text heavy pages: ie www.peter-lindqvist.net/somatic-articles and www.peter-lindqvist.net/client-reviews
My effort at redesigning is underway here: https://pjlindqvist.sitebuilderhost.net/my-site-7
The original sitebuilder template is this one: https://www.sitebuilderhost.net/website-template/view/html/4917?originUrl=https%3A%2F%2Fwww.sitebuilderhost.net%2Fwebsite%2Ftemplates%2Fhtml%2Fhealth-wellness&tpClick=view_button&esi=8a41c27d-03e9-4c6b-b1f2-9d5e02a7c4f3
I'm pretty happy with the colour palette. My name Peter Joseph Lindqvist is now the "brand" without Rooted Stillness subtitle. Regarding the Welcome section, if you are going to use my photos, it probably needs to be those two that are already there. If you want to put a stock photo there instead, that's fine.
If you want to propose something quite different to my design, I'm happy to receive design files in Photoshop or whatever and then subsequently replicate on Sitebuilder. Up to you.
Mostly women, some men ages 28-60.

```html
<!DOCTYPE html>
<html lang="en">
<head>
<meta charset="utf-8">
<title>Peter Lindqvist – Rooted Stillness Teacher</title>
<link href="https://fonts.googleapis.com/css2?family=Montserrat:wght@500;600;700;800&family=Poppins:wght@400;500;600&display=swap" rel="stylesheet">
<style>
:root{
  --gold:#b98a35;
  --gold-dark:#9c6f22;
  --gold-grad:linear-gradient(90deg,#a97a28,#d3a650);
  --cream:#f6eee0;
  --ink:#161616;
  --body:#555;
  --line:#e3d8c6;
  --white:#fff;
}
*{box-sizing:border-box;margin:0;padding:0}
html,body{width:1200px;height:4860px;overflow:hidden;background:var(--white)}
body{font-family:"Poppins",sans-serif;color:var(--body);position:relative}
section,header,footer{position:absolute;left:0;width:1200px}
.heading{font-family:"Montserrat",sans-serif;font-weight:700;color:var(--ink);line-height:1.05}
.btn{display:inline-flex;align-items:center;gap:16px;background:var(--gold-grad);color:#fff;font-family:"Montserrat",sans-serif;font-weight:600;font-size:17px;letter-spacing:.5px;padding:0 12px 0 28px;height:60px;border-radius:30px;text-transform:uppercase;white-space:nowrap}
.btn .btn-icon{width:34px;height:34px;border-radius:50%;background:#fff;display:flex;align-items:center;justify-content:center}
.btn.small{height:46px;font-size:14px;padding:0 8px 0 22px}
.btn.small .btn-icon{width:30px;height:30px}
.photo{position:absolute}
.text-body{font-size:15px;line-height:1.75;color:var(--body)}
.sub{font-family:"Montserrat",sans-serif;font-weight:700;color:var(--ink);font-size:27px;line-height:1.3}

/* header */
.site-header{top:0;height:152px;background:#fff}
.brand{position:absolute;left:44px;top:28px;display:flex;flex-direction:column;align-items:center;width:190px}
.brand-dot{width:42px;height:42px;border-radius:50%;background:var(--gold);margin-bottom:10px}
.brand-name{font-family:"Montserrat",sans-serif;font-weight:700;font-size:24px;color:var(--ink);letter-spacing:1px;white-space:nowrap}
.nav{position:absolute;right:44px;top:54px;display:flex;align-items:center;gap:34px;font-family:"Montserrat",sans-serif;font-size:15px;font-weight:600;color:var(--ink)}
.nav .active{color:var(--gold);border-bottom:2px solid var(--gold);padding-bottom:4px}
.nav .btn{height:46px;font-size:14px;padding:0 26px}

/* hero */
.hero{top:152px;height:680px;background:var(--cream)}
.hero-copy{position:absolute;left:96px;top:126px;width:480px}
.eyebrow{font-family:"Montserrat",sans-serif;font-weight:700;color:var(--gold);font-size:22px;letter-spacing:1px;margin-bottom:14px}
.hero h1{font-size:46px;font-weight:800;white-space:nowrap}
.hero h1 .gold{color:var(--gold)}
.hero h1 .case{text-transform:none}
.hero p{margin:18px 0 36px;font-size:16px;line-height:1.6}
.hero .photo{left:600px;top:0;width:600px;height:680px;background:linear-gradient(135deg,#caa992,#8a7a7f 45%,#473a5a 75%,#d9c4b4)}

/* practice */
.practice{top:832px;height:748px}
.practice .frame{position:absolute;left:120px;top:120px;width:410px;height:410px;border:4px solid var(--gold)}
.practice .photo{left:88px;top:148px;width:412px;height:448px;background:linear-gradient(160deg,#9aa09a,#c8b8a6 50%,#6b6a63)}
.practice .copy{position:absolute;left:612px;top:150px;width:520px}
.copy h2{font-size:62px;margin-bottom:30px;white-space:nowrap}
.copy .sub{margin-bottom:22px}
.copy .text-body{margin-bottom:20px}

/* about */
.about{top:1580px;height:680px;background:var(--cream)}
.about .photo{left:0;top:0;width:600px;height:680px;background:linear-gradient(150deg,#5f7b4d,#9a8465 55%,#3f4a32)}
.about .copy{left:662px;top:100px;position:absolute;width:480px}

/* approach */
.approach{top:2260px;height:700px;background:var(--cream)}
.approach .copy{position:absolute;left:92px;top:130px;width:470px}
.approach .copy h2{font-size:58px}
.approach .photo{left:600px;top:0;width:600px;height:700px;background:linear-gradient(140deg,#7d8d77,#c9b6a4 45%,#4b3d5c 75%,#a89a8e)}

/* reviews */
.reviews{top:2960px;height:620px;text-align:center}
.reviews h2{font-size:60px;margin-top:120px}
.divider{display:block;margin:14px auto 0}
.arrow{position:absolute;top:336px;width:40px;height:40px;border-radius:50%;display:flex;align-items:center;justify-content:center}
.arrow.prev{left:72px;background:#f0e6d6}
.arrow.next{right:72px;background:var(--gold)}
.quote-mark{position:absolute;left:196px;top:250px;font-family:"Montserrat",sans-serif;font-weight:800;font-size:240px;line-height:.8;color:var(--gold)}
.review-text{position:absolute;left:362px;top:262px;width:720px;text-align:left;font-size:15px;line-height:1.8}
.reviewer{position:absolute;left:480px;top:410px;display:flex;align-items:center;gap:18px}
.avatar{width:80px;height:80px;border-radius:50%;background:linear-gradient(135deg,#c88b62,#6c4a33)}
.reviewer-name{font-family:"Montserrat",sans-serif;font-weight:600;color:var(--gold);font-size:18px;text-align:left}
.stars{display:flex;gap:3px;margin-top:4px}

/* contact */
.contact{top:3580px;height:800px;background:var(--cream);text-align:center}
.contact h2{font-size:62px;margin-top:110px}
.contact .lead{margin-top:30px;font-size:19px;color:#444}
.form{position:absolute;left:180px;top:320px;width:848px}
.field{position:absolute;background:#fff;border-radius:6px;height:62px;display:flex;align-items:center;gap:18px;padding-left:26px;font-size:16px;color:#777;box-shadow:0 2px 6px rgba(0,0,0,.05)}
.contact .btn{position:absolute;left:498px;top:652px;padding:0 12px 0 30px}

/* footer */
.site-footer{top:4380px;height:480px;background:#fff}
.site-footer .brand{left:505px;top:44px}
.footer-info{position:absolute;left:208px;top:196px;width:820px;display:flex;justify-content:space-between}
.info{display:flex;align-items:center;gap:18px;font-size:14px;color:#333;text-align:left;line-height:1.5}
.info .icon{width:46px;height:46px;background:var(--gold);display:flex;align-items:center;justify-content:center;flex-shrink:0}
.info strong{font-family:"Montserrat",sans-serif;font-weight:700;font-size:13px;display:block;color:var(--ink)}
.footer-rule{position:absolute;left:60px;top:300px;width:1080px;border-top:1px solid var(--line)}
.footer-nav{position:absolute;left:0;width:1200px;top:336px;display:flex;justify-content:center;gap:60px;font-family:"Montserrat",sans-serif;font-weight:600;font-size:14px;color:var(--ink)}
.footer-bottom{position:absolute;left:60px;top:400px;width:1080px;border-top:1px solid var(--line);padding-top:22px;font-size:13px;color:#444;display:flex;justify-content:space-between;align-items:center}
.socials{display:flex;gap:8px}
.socials span{width:24px;height:24px;background:var(--gold);display:block}
</style>
</head>
<body>

<header class="site-header">
  <div class="brand"><span class="brand-dot"></span><span class="brand-name">PETER LINDQVIST</span></div>
  <nav class="nav">
    <span class="active">HOME</span><span>THE PRACTICE</span><span>ABOUT ME</span><span>FEEDBACK</span><span>APPROACH</span>
    <span class="btn">Contact Me</span>
  </nav>
</header>

<section class="hero">
  <div class="hero-copy">
    <div class="eyebrow">PETER LINDQVIST</div>
    <h1 class="heading">GREATER SUCCESS<br><span class="gold">IN WORK AND</span><br><span class="case">Professional Life</span></h1>
    <p>Lorem ipsum dolor sit amet, consectetur adipiscing elit, sed do eiusmod tempor incididunt ut labore et dolore magna aliqua. Quis ipsum suspendisse ultrices gravida.</p>
    <span class="btn">Contact Me <span class="btn-icon"><svg width="16" height="16" viewBox="0 0 16 16"><path d="M5 3l5 5-5 5" fill="none" stroke="#b98a35" stroke-width="2"/></svg></span></span>
  </div>
  <div class="photo" role="img" aria-label="Hands of a practitioner resting on a client's back during a bodywork session"></div>
</section>

<section class="practice">
  <div class="frame"></div>
  <div class="photo" role="img" aria-label="Practitioner gently holding a client's head as she lies on a treatment table"></div>
  <div class="copy">
    <h2 class="heading">THE PRACTICE</h2>
    <div class="sub">A session typically begins by clarifying your intention or wish.</div>
    <p class="text-body">You may be facing physical or emotional challenges or seeking help with another aspect of your life, such as family or relationship patterns.</p>
    <p class="text-body">With your intention in the work clarified, I will assess how energy is flowing in your body and where there are blockages in the physical structure.</p>
    <span class="btn small">Read More <span class="btn-icon"><svg width="14" height="14" viewBox="0 0 16 16"><path d="M5 3l5 5-5 5" fill="none" stroke="#b98a35" stroke-width="2"/></svg></span></span>
  </div>
</section>

<section class="about">
  <div class="photo" role="img" aria-label="Portrait of the practitioner outdoors among green plants"></div>
  <div class="copy">
    <h2 class="heading">ABOUT ME</h2>
    <div class="sub">Rooted Stillness® Teacher</div>
    <p class="text-body">Growing up in Scotland I had a strong connection with nature and the outdoors. Playing outside with friends, with bikes, ball sports, and later mountaineering and rock climbing, was what most interested me.</p>
    <p class="text-body">I studied at Northgate University and worked in London for a number of years as a civil servant. I subsequently set up a property business and in 2005, relocated to Spain.</p>
    <span class="btn small">Read More <span class="btn-icon"><svg width="14" height="14" viewBox="0 0 16 16"><path d="M5 3l5 5-5 5" fill="none" stroke="#b98a35" stroke-width="2"/></svg></span></span>
  </div>
</section>

<section class="approach">
  <div class="copy">
    <h2 class="heading">APPROACH TO<br>HEALING</h2>
    <div class="sub" style="font-size:25px">My work is inspired by a modality called Rooted Stillness®.</div>
    <p class="text-body">It's a way of exploring how we create and interpret our experience of ourselves and the world around us. A way of locating the source of limiting beliefs and behaviours to broaden choice and possibility in our lives now.</p>
    <span class="btn small">Read More <span class="btn-icon"><svg width="14" height="14" viewBox="0 0 16 16"><path d="M5 3l5 5-5 5" fill="none" stroke="#b98a35" stroke-width="2"/></svg></span></span>
  </div>
  <div class="photo" role="img" aria-label="Practitioner working on a client's legs on a treatment table"></div>
</section>

<section class="reviews">
  <h2 class="heading">CUSTOMER REVIEWS</h2>
  <svg class="divider" width="140" height="20" viewBox="0 0 140 20"><line x1="0" y1="10" x2="56" y2="10" stroke="#b98a35"/><circle cx="70" cy="10" r="7" fill="#b98a35"/><line x1="84" y1="10" x2="140" y2="10" stroke="#b98a35"/></svg>
  <span class="arrow prev"><svg width="14" height="14" viewBox="0 0 16 16"><path d="M11 3L6 8l5 5" fill="none" stroke="#b98a35" stroke-width="2"/></svg></span>
  <span class="arrow next"><svg width="14" height="14" viewBox="0 0 16 16"><path d="M5 3l5 5-5 5" fill="none" stroke="#fff" stroke-width="2"/></svg></span>
  <div class="quote-mark">&ldquo;</div>
  <p class="review-text">In 20 years as a bodyworker I've never felt something like this... It's so beautiful, so complete. The change I've noticed is that in some way what I knew mentally is now integrated. I feel more connected... I trust more... I know that everything is going to be OK. It really resonates with me and I'm keen to learn more.</p>
  <div class="reviewer">
    <div class="avatar" role="img" aria-label="Client portrait"></div>
    <div>
      <div class="reviewer-name">Mara Ellison</div>
      <div class="stars">
        <svg width="90" height="16" viewBox="0 0 90 16"><g fill="#e0a52b"><path id="s" d="M8 0l2.4 5 5.6.6-4.2 3.8 1.2 5.6L8 12.2 3 15l1.2-5.6L0 5.6 5.6 5z"/><use href="#s" x="18"/><use href="#s" x="36"/><use href="#s" x="54"/><use href="#s" x="72"/></g></svg>
      </div>
    </div>
  </div>
</section>

<section class="contact">
  <h2 class="heading">CONTACT ME</h2>
  <svg class="divider" width="140" height="20" viewBox="0 0 140 20"><line x1="0" y1="10" x2="56" y2="10" stroke="#b98a35"/><circle cx="70" cy="10" r="7" fill="#b98a35"/><line x1="84" y1="10" x2="140" y2="10" stroke="#b98a35"/></svg>
  <p class="lead">Contact me for more information about intensives or to arrange an appointment.</p>
  <div class="form">
    <div class="field" style="left:0;top:0;width:416px"><svg width="16" height="16" viewBox="0 0 16 16"><circle cx="8" cy="5" r="3.5" fill="#666"/><path d="M1 16c0-4 3-6 7-6s7 2 7 6z" fill="#666"/></svg>First Name</div>
    <div class="field" style="left:428px;top:0;width:420px"><svg width="18" height="14" viewBox="0 0 18 14"><rect x="0" y="0" width="18" height="14" rx="1" fill="#666"/><path d="M1 1l8 6 8-6" fill="none" stroke="#fff" stroke-width="1.5"/></svg>E-Mail</div>
    <div class="field" style="left:0;top:78px;width:416px"><svg width="16" height="16" viewBox="0 0 16 16"><path d="M3 1l3 3-2 2c1 2 3 4 5 5l2-2 3 3-2 3C7 15 1 9 1 3z" fill="#666"/></svg>Phone Number</div>
    <div class="field" style="left:428px;top:78px;width:420px"><svg width="14" height="18" viewBox="0 0 14 18"><path d="M7 0a7 7 0 017 7c0 5-7 11-7 11S0 12 0 7a7 7 0 017-7z" fill="#666"/><circle cx="7" cy="7" r="2.5" fill="#fff"/></svg>Address</div>
    <div class="field" style="left:0;top:156px;width:848px;height:128px;align-items:flex-start;padding-top:20px"><svg width="16" height="16" viewBox="0 0 16 16"><path d="M1 15l1-4 9-9 3 3-9 9z" fill="#666"/></svg>Message</div>
  </div>
  <span class="btn">Submit Now <span class="btn-icon"><svg width="16" height="16" viewBox="0 0 16 16"><path d="M5 3l5 5-5 5" fill="none" stroke="#b98a35" stroke-width="2"/></svg></span></span>
</section>

<footer class="site-footer">
  <div class="brand"><span class="brand-dot"></span><span class="brand-name">PETER LINDQVIST</span></div>
  <div class="footer-info">
    <div class="info"><span class="icon"><svg width="18" height="18" viewBox="0 0 16 16"><path d="M3 1l3 3-2 2c1 2 3 4 5 5l2-2 3 3-2 3C7 15 1 9 1 3z" fill="#fff"/></svg></span><div><strong>CALL US</strong>+351 910 204 377</div></div>
    <div class="info"><span class="icon"><svg width="20" height="15" viewBox="0 0 18 14"><rect width="18" height="14" rx="1" fill="#fff"/><path d="M1 1l8 6 8-6" fill="none" stroke="#b98a35" stroke-width="1.5"/></svg></span><div><strong>EMAIL US</strong>info@peter-lindqvist.net</div></div>
    <div class="info"><span class="icon"><svg width="15" height="19" viewBox="0 0 14 18"><path d="M7 0a7 7 0 017 7c0 5-7 11-7 11S0 12 0 7a7 7 0 017-7z" fill="#fff"/><circle cx="7" cy="7" r="2.5" fill="#b98a35"/></svg></span><div>Rua das Flores 12, Estrela<br>Lisbon, Portugal, 1200-001</div></div>
  </div>
  <div class="footer-rule"></div>
  <nav class="footer-nav"><span>THE PRACTICE</span><span>ABOUT ME</span><span>FEEDBACK</span><span>APPROACH</span><span>CONTACT</span></nav>
  <div class="footer-bottom">
    <span>© Peter Joseph Lindqvist 2023 &nbsp;|&nbsp; "Rooted Stillness®" is a trademark of Quiet Field Studio LLC</span>
    <div class="socials"><span></span><span></span><span></span><span></span></div>
  </div>
</footer>

</body>
</html>
```